2.875 x 4 inch Ad for a Program Guide at Conference with 15,000

The ad needs to be 2.875 inches by 4 inches. I have attached some ideas. We definitely don't want a white background but we need the ad to visually jump off a page so our ad doesn't get lost. The mock-ups were something I put together so I could get a sense of what I wanted to say. I've also attached feedback from my business partners about these mock-ups.

Target Market(s)

Heads of Human Resources and Leadership Development, CEO's, COO's, and business owners.

Industry/Entity Type

Consulting

Font styles to use
Serif

Colors
6b449b
0355a3
0692cd
00a990
a64599
f37122

Requirements
Must have
• Colors from brand standards. Logo. Large lettering to be seen easily as a quarter page ad.
Nice to have
• Creativity... feeling of strength, warmth and business all at the same time.
Should not have
• Please note the updated logo. The name of the company is Varondi Mindful Trade.

```html
<!DOCTYPE html>
<html lang="en">
<head>
<meta charset="utf-8">
<title>Varondi Mindful Trade – Leadership &amp; Culture Ad</title>
<link rel="stylesheet" href="https://fonts.googleapis.com/css2?family=Noto+Sans:wght@300;400;700;800&display=swap">
<style>
  :root {
    --ice: #cfe9ea;
    --ice-deep: #4fb3d8;
    --ocean: #5678a8;
    --teal: #52b59c;
    --navy: #2b3f7c;
    --orange: #f0a463;
    --plum: #6a2a66;
    --white: #ffffff;
  }
  * { margin: 0; padding: 0; box-sizing: border-box; }
  html, body { width: 862px; height: 1200px; overflow: hidden; background: #ffffff; }
  .ad {
    position: relative;
    width: 862px;
    height: 1200px;
    overflow: hidden;
    font-family: "Noto Sans", "DejaVu Sans", Verdana, sans-serif;
  }
  .texture-panel {
    position: absolute; left: 0; top: 0; width: 402px; height: 1200px;
    background: linear-gradient(170deg, #d8ecea 0%, var(--ice) 35%, #9fd6e4 70%, var(--ice-deep) 100%);
  }
  .colour-panel {
    position: absolute; left: 402px; top: 0; width: 460px; height: 1200px;
    background: linear-gradient(180deg, var(--ocean) 0%, #5a8aa8 40%, #55a8a6 75%, var(--teal) 100%);
  }
  .brand {
    position: absolute; left: 0; width: 862px; top: 100px;
    display: flex; justify-content: center; align-items: center; gap: 18px;
  }
  .brand-dot {
    width: 64px; height: 64px; border-radius: 50%;
    border: 6px solid var(--navy);
  }
  .brand-name {
    font-size: 42px; font-weight: 700; color: var(--navy); letter-spacing: 1px;
  }
  .verb {
    position: absolute; left: 144px; white-space: nowrap;
    color: var(--white); font-weight: 800; line-height: 1;
    text-transform: uppercase;
  }
  .verb--explore { top: 271px; font-size: 113px; letter-spacing: 11px; }
  .verb--develop { top: 385px; font-size: 113px; letter-spacing: 11px; }
  .verb--strengthen { top: 500px; font-size: 77px; letter-spacing: 7px; }
  .topic {
    position: absolute; left: 144px; color: var(--orange); white-space: nowrap;
    font-weight: 800; font-size: 98px; line-height: 1; letter-spacing: 4.5px;
  }
  .topic--leadership { top: 654px; }
  .topic--culture { top: 774px; }
  .learn {
    position: absolute; left: 144px; top: 905px;
    font-size: 34px; font-weight: 300; color: var(--plum); line-height: 1;
  }
  .formula {
    position: absolute; color: var(--plum); font-weight: 700; font-size: 34px;
    line-height: 1; letter-spacing: 0.7px; white-space: nowrap;
  }
  .formula--plus { left: 400px; top: 928px; }
  .formula--leadership { left: 436px; top: 905px; }
  .formula--culture { left: 436px; top: 941px; }
  .formula--result { left: 400px; top: 1000px; }
  .contact {
    position: absolute; left: 0; width: 866px; text-align: center;
    color: var(--plum); font-size: 31px; font-weight: 300; line-height: 1;
  }
  .contact--booth { top: 1077px; }
  .contact--web { top: 1118px; }
</style>
</head>
<body>
  <main class="ad">
    <div class="texture-panel" role="img" aria-label="Soft icy blue marbled texture"></div>
    <div class="colour-panel"></div>

    <header class="brand">
      <span class="brand-dot"></span>
      <span class="brand-name">Varondi Mindful Trade</span>
    </header>

    <h1>
      <span class="verb verb--explore">Explore</span>
      <span class="verb verb--develop">Develop</span>
      <span class="verb verb--strengthen">Strengthen</span>
    </h1>

    <h2>
      <span class="topic topic--leadership">Leadership</span>
      <span class="topic topic--culture">&amp; Culture</span>
    </h2>

    <p class="learn">Learn how:</p>
    <span class="formula formula--plus">+</span>
    <span class="formula formula--leadership">REAL Leadership</span>
    <span class="formula formula--culture">REAL Culture</span>
    <span class="formula formula--result">= REAL Results</span>

    <p class="contact contact--booth">Booth 418</p>
    <p class="contact contact--web">www.varondigroup.com</p>
  </main>
</body>
</html>
```